依頼詳細
ホームページ料金の価格破壊を行いたいです。納品が1週間以内で早い!!イラストよりも写真を使ってほしいです。
記載項目
社名等も入れますが、上記の内容を考慮して作っていただけると助かります。
よろしくお願いいたします。
サイズ
A4
ページ数
片面
希望イメージ
シンプル 複雑
単色 カラフル
暗い 明るい
日常 高級
遊び心 厳粛
未来的 伝統的
女性的 男性的
希望する色
お任せいたします。
納品ファイル
• 高解像度JPG (.jpg)
• イラストレーター形式 (.ai)
〒471-0093
大阪市淀川区東川原3-4-17
ミツバ第2北梅田4階
0120-914-562
この住所を明記ください。
月々の料金なし!!ポッキリ 5万円!!
プロの作ったホームページが5万円!!みたいな
友達に作ってもらった安かろう悪かろうではなく、本当の高品質なホームページが作れる集団です。みたいなことを入れてほしい。

写真が奇麗でいいなあ!と思いました。

他にも良いデザインがたくさんありました。迷いましたが・・・・みなさんありがとうございました。

```html
<!DOCTYPE html>
<html lang="ja">
<head>
<meta charset="utf-8">
<title>ソラウェブ ホームページ制作 5万円</title>
<link href="https://fonts.googleapis.com/css2?family=Noto+Sans+JP:wght@400;700;900&display=swap" rel="stylesheet">
<style>
  :root {
    --brand-blue: #1b7fd0;
    --box-blue: #1f8fe0;
    --deep-blue: #0d4f8f;
    --price-red: #e60012;
    --ink: #111;
    --paper: #fff;
    --grey-bar: #8e9aa4;
  }
  * { margin: 0; padding: 0; box-sizing: border-box; }
  html, body { width: 849px; height: 1200px; overflow: hidden; background: var(--paper); }
  body { font-family: "Noto Sans JP", sans-serif; color: var(--ink); }
  .flyer { position: relative; width: 849px; height: 1200px; overflow: hidden; background: var(--paper); }

  .header { position: absolute; top: 0; left: 0; width: 100%; height: 56px; display: flex; align-items: center; padding: 0 22px; border-bottom: 2px solid var(--brand-blue); }
  .brand { display: flex; align-items: center; gap: 8px; color: var(--brand-blue); font-weight: 700; font-size: 24px; letter-spacing: 0.02em; }
  .brand-dot { width: 22px; height: 22px; border-radius: 50%; background: var(--brand-blue); }
  .header-tagline { margin-left: 22px; font-size: 10.5px; color: #444; white-space: nowrap; }

  .url-bar { position: absolute; top: 62px; left: 22px; right: 22px; height: 34px; display: flex; }
  .url-box { flex: 0 0 470px; border: 2px solid #555; background: var(--paper); font-size: 19px; font-weight: 700; display: flex; align-items: center; padding-left: 12px; }
  .url-fill { flex: 1; background: linear-gradient(#b7c0c8, var(--grey-bar)); border: 2px solid #555; border-left: none; }

  .hero { position: absolute; top: 100px; left: 0; width: 100%; height: 640px; }
  .hero-photo { position: absolute; inset: 0; background: linear-gradient(170deg, #dfeefa 0%, #8fbde6 30%, #3f7fc0 62%, #1c3f6e 100%); }
  .hero-lead { position: absolute; top: 6px; left: 22px; font-size: 19px; font-weight: 700; color: var(--ink); }
  .hero-note { position: absolute; top: 30px; right: 70px; font-size: 16px; font-weight: 700; color: var(--price-red); background: rgba(255,255,255,.85); padding: 0 6px; }
  .breaking { position: absolute; top: 66px; left: 24px; width: 92px; height: 496px; background: var(--paper); display: flex; flex-direction: column; justify-content: space-around; align-items: center; font-size: 84px; font-weight: 900; line-height: 1; color: var(--ink); }
  .pokkiri { position: absolute; top: 58px; right: 120px; font-size: 50px; font-weight: 900; color: var(--price-red); font-style: italic; -webkit-text-stroke: 2px var(--paper); paint-order: stroke fill; transform: rotate(-6deg); }
  .price-five { position: absolute; top: 60px; left: 230px; width: 360px; height: 560px; }
  .price-unit { position: absolute; top: 200px; right: 140px; display: flex; flex-direction: column; font-size: 122px; font-weight: 900; line-height: 1.05; color: var(--price-red); -webkit-text-stroke: 8px var(--paper); paint-order: stroke fill; }
  .price-tax { position: absolute; top: 566px; right: 120px; font-size: 17px; font-weight: 700; color: var(--price-red); background: rgba(255,255,255,.85); padding: 0 6px; }

  .speed { position: absolute; top: 748px; left: 0; width: 100%; text-align: center; font-size: 46px; font-weight: 900; letter-spacing: 0.02em; }

  .features { position: absolute; top: 818px; left: 22px; right: 22px; height: 196px; display: flex; gap: 14px; }
  .feature { flex: 1; background: var(--box-blue); color: var(--paper); border-radius: 10px; display: flex; flex-direction: column; justify-content: center; align-items: center; text-align: center; font-weight: 900; line-height: 1.2; }
  .feature-small { font-size: 27px; }
  .feature-big { font-size: 62px; margin-top: 6px; }
  .feature-mid { font-size: 44px; }

  .footer { position: absolute; top: 1024px; left: 0; width: 100%; height: 176px; border-top: 3px solid var(--brand-blue); }
  .footer-call { position: absolute; top: 14px; left: 22px; font-size: 17px; font-weight: 700; color: var(--brand-blue); }
  .footer-brand { position: absolute; top: 62px; left: 22px; font-size: 38px; }
  .footer-brand .brand-dot { width: 34px; height: 34px; }
  .footer-company { position: absolute; top: 118px; left: 66px; font-size: 12px; color: var(--brand-blue); font-weight: 700; }
  .tel { position: absolute; top: 42px; right: 22px; font-size: 64px; font-weight: 900; color: var(--brand-blue); letter-spacing: -0.01em; }
  .tel-label { font-size: 46px; }
  .address { position: absolute; top: 128px; right: 22px; font-size: 14px; color: #333; }
</style>
</head>
<body>
<div class="flyer">
  <header class="header">
    <div class="brand"><span class="brand-dot"></span>sora web</div>
    <p class="header-tagline">－ | 株式会社ソラウェブ | 日本の集客を変える、ソラウェブ月額固定制のSEO対策！</p>
  </header>

  <div class="url-bar">
    <div class="url-box">http://www.sorawebworks.jp/service.html</div>
    <div class="url-fill"></div>
  </div>

  <section class="hero">
    <div class="hero-photo" role="img" aria-label="青空を見上げる高層ビル群の写真"></div>
    <p class="hero-lead">プロの作ったホームページが・・・</p>
    <p class="hero-note">↑実例はホームページで！</p>
    <h1 class="breaking"><span>価</span><span>格</span><span>破</span><span>壊</span></h1>
    <p class="pokkiri">ポッキリ</p>
    <svg class="price-five" viewBox="0 0 360 560" aria-label="5">
      <text x="180" y="520" text-anchor="middle" font-family="Noto Sans JP, sans-serif" font-weight="900" font-size="640" fill="#e60012" stroke="#fff" stroke-width="14" paint-order="stroke fill">5</text>
    </svg>
    <p class="price-unit"><span>万</span><span>円</span></p>
    <p class="price-tax">(税込 52,500 円)</p>
  </section>

  <h2 class="speed">納期が１週間以内で早い！</h2>

  <section class="features">
    <div class="feature">
      <span class="feature-small">ドメイン取得料</span>
      <span class="feature-small">サーバー設定料</span>
      <span class="feature-big">無料</span>
    </div>
    <div class="feature">
      <span class="feature-mid">SEO</span>
      <span class="feature-mid">対策も</span>
      <span class="feature-mid">お任せ！</span>
    </div>
    <div class="feature">
      <span class="feature-small" style="font-size:38px">月額料金</span>
      <span class="feature-big" style="font-size:72px">なし</span>
    </div>
  </section>

  <footer class="footer">
    <p class="footer-call">いつでもお気軽にご相談下さい→</p>
    <div class="brand footer-brand"><span class="brand-dot"></span>sora web</div>
    <p class="footer-company">株式会社ソラウェブ</p>
    <p class="tel"><span class="tel-label">TEL</span>0120-914-562</p>
    <p class="address">〒471-0093　大阪市淀川区東川原3-4-17　ミツバ第2北梅田4階</p>
  </footer>
</div>
</body>
</html>
```